Small CPA firm
Project: Business cards and stationary
Business cards and stationary - Financial Services
Business cards and stationary
Professional
Darren P. Holcomb
Certified Public Accountant
418 Birchmont Lane, 4-120 Mobile, Alabama 36609
dh@dholcombcpa.example
www.dholcombcpa.example
I'd like a professional but creative looking business card and stationary using my logo. For the business card, I think I would like a design with the logo on the top or the left side, with my name and contact information on the bottom (for logo on top) or right hand side (for logo on left). I'd like to use the same primary colors that the logo uses.
For the back of the card, I think I'd like just the logo without the words in an appropriate format.

```html
<!DOCTYPE html>
<html lang="en">
<head>
<meta charset="utf-8">
<title>Darren P. Holcomb CPA LLC — Business Card</title>
<link href="https://fonts.googleapis.com/css2?family=Cinzel:wght@400;600&family=Open+Sans:wght@400;600&display=swap" rel="stylesheet">
<style>
  :root {
    --bg: #e9e6e2;
    --card-white: #ffffff;
    --brand-blue: #1a9ccf;
    --brand-blue-light: #2bb0e0;
    --brand-blue-dark: #0f7fae;
    --ink: #3f4448;
    --ink-soft: #5b6166;
    --silver: #9aa3aa;
  }
  * { box-sizing: border-box; margin: 0; padding: 0; }
  html, body { width: 1200px; height: 576px; overflow: hidden; }
  body { background: var(--bg); position: relative; font-family: "Open Sans", sans-serif; }

  .card {
    position: absolute; top: 140px; width: 516px; height: 296px; overflow: hidden;
  }
  .card--front { left: 72px; background: var(--card-white); }
  .card--back {
    left: 612px;
    background: radial-gradient(circle at 50% 48%, var(--brand-blue-light) 0%, var(--brand-blue) 55%, var(--brand-blue-dark) 100%);
  }

  /* Front */
  .brand { position: absolute; left: 20px; top: 32px; display: flex; align-items: center; gap: 12px; }
  .brand__mark {
    width: 64px; height: 64px; border-radius: 50%; flex: none;
    background: radial-gradient(circle at 35% 30%, #e4e8eb, var(--silver));
  }
  .brand__name {
    font-family: "Cinzel", serif; font-weight: 600; font-size: 21px; color: var(--ink);
    line-height: 1.1; white-space: nowrap;
  }
  .brand__tagline {
    font-family: "Cinzel", serif; font-size: 12px; color: var(--ink-soft); margin-top: 4px;
    letter-spacing: 0.3px; white-space: nowrap;
  }

  .band { position: absolute; left: 0; top: 128px; width: 516px; height: 168px; }
  .holder {
    position: absolute; left: 128px; top: 146px; font-size: 14px; color: #fff; letter-spacing: 0.5px;
    white-space: nowrap;
  }
  .holder__title { color: var(--ink); font-size: 12.5px; margin-left: 10px; letter-spacing: 0; }

  .contact {
    position: absolute; left: 40px; right: 14px; top: 196px; text-align: right;
    font-size: 11px; line-height: 20px; color: var(--ink); white-space: nowrap;
  }
  .contact__label { color: var(--brand-blue); font-weight: 600; }
  .contact__link { color: var(--brand-blue); }

  /* Back */
  .back-mark {
    position: absolute; left: 50%; top: 50%; width: 92px; height: 92px; margin: -60px 0 0 -46px;
    border-radius: 50%; background: radial-gradient(circle at 35% 30%, #eef1f3, var(--silver));
    box-shadow: 0 2px 6px rgba(0,0,0,0.2);
  }
  .back-url {
    position: absolute; left: 0; right: 0; bottom: 42px; text-align: center;
    color: #fff; font-size: 12px; letter-spacing: 3px;
  }
</style>
</head>
<body>
  <section class="card card--front" aria-label="Business card front">
    <div class="brand">
      <div class="brand__mark"></div>
      <div>
        <div class="brand__name">Darren P. Holcomb CPA LLC</div>
        <div class="brand__tagline">Certified Public Accountant and Advisor</div>
      </div>
    </div>

    <svg class="band" viewBox="0 0 516 168" aria-hidden="true">
      <path d="M0 0 H516 V20 H0 Z" fill="var(--brand-blue-light)" opacity="0.35"/>
      <path d="M110 14 Q100 14 96 24 L92 52 H516 V14 Z" fill="var(--brand-blue)"/>
      <path d="M0 52 H120 Q100 56 96 90 L92 168 H0 Z" fill="var(--brand-blue)" opacity="0.12"/>
    </svg>

    <div class="holder">DARREN P. HOLCOMB<span class="holder__title">Certified Public Accountant</span></div>

    <div class="contact">
      <div>418 Birchmont Lane, 4-120 Mobile, Alabama 36609</div>
      <div><span class="contact__label">Ph.:</span> (251) 555-0142 &nbsp;<span class="contact__label">C.:</span> (251) 555-0187</div>
      <div><span class="contact__label">F.:</span> (251) 555-0163 &nbsp;<span class="contact__label">E.:</span> dh@dholcombcpa.example &nbsp;<span class="contact__link">www.dholcombcpa.example</span></div>
    </div>
  </section>

  <section class="card card--back" aria-label="Business card back">
    <div class="back-mark"></div>
    <div class="back-url">www.dholcombcpa.example</div>
  </section>
</body>
</html>
```